Broadcaster,Conference Host,Facilitator

Looking for a business card and logo to create the Grant Felber brand .. Something with a slant towards radio and conference speaking
I like the idea of classic black white or grey but open to suggestions

Target Market(s)

Corporates

Industry/Entity Type

Business

Contact Information for Business Card

Grant Felber
Email : Grant.Felber@quorvamail.co.uk
Mobile : +44 7700 382046
Twitter : @Grantfelber

Font styles to use
Serif
Decorative
Script

Requirements
Must have
• Feel classy and dynamic
Should not have
• Cartoons

```html
<!DOCTYPE html>
<html lang="en">
<head>
<meta charset="utf-8">
<title>Grant Felber — Business Card</title>
<link rel="stylesheet" href="https://fonts.googleapis.com/css2?family=Josefin+Slab:wght@400;600;700&display=swap">
<style>
  :root {
    --ink: #1f1d1e;
    --paper: #ffffff;
    --signal-red: #e21b22;
    --stage: #dcd9d5;
    --text-light: #f2f2f2;
  }
  html, body {
    margin: 0;
    padding: 0;
    width: 1200px;
    height: 900px;
    overflow: hidden;
    background: var(--stage);
    font-family: "Josefin Slab", Georgia, serif;
  }
  .canvas {
    position: relative;
    width: 1200px;
    height: 900px;
  }
  .card {
    position: absolute;
    left: 250px;
    width: 700px;
    height: 400px;
    overflow: hidden;
    box-shadow: 0 6px 18px rgba(0,0,0,0.18);
  }
  .card--front { top: 30px; background: var(--paper); }
  .card--back { top: 470px; background: var(--ink); }

  .front-shape { position: absolute; inset: 0; }

  .brand-mark {
    position: absolute;
    left: 0;
    width: 300px;
    top: 55px;
    display: flex;
    flex-direction: column;
    align-items: center;
  }
  .brand-mark__circle {
    width: 150px;
    height: 150px;
    border-radius: 50%;
    background: var(--signal-red);
  }
  .brand-mark__name {
    margin-top: 22px;
    font-size: 30px;
    font-weight: 600;
    color: var(--ink);
    letter-spacing: 0.5px;
    white-space: nowrap;
  }

  .contact {
    position: absolute;
    left: 380px;
    right: 24px;
    top: 122px;
    color: var(--text-light);
  }
  .contact__name {
    font-size: 32px;
    font-weight: 600;
    color: var(--signal-red);
    margin: 0 0 12px;
    letter-spacing: 0.5px;
    white-space: nowrap;
  }
  .contact__list { list-style: none; margin: 0; padding: 0; }
  .contact__item {
    display: flex;
    align-items: center;
    gap: 11px;
    font-size: 18px;
    line-height: 25px;
    white-space: nowrap;
  }
  .contact__item svg { flex: none; }

  .back-mark {
    position: absolute;
    inset: 0;
    display: flex;
    flex-direction: column;
    align-items: center;
    justify-content: center;
  }
  .back-mark__circle {
    width: 240px;
    height: 240px;
    border-radius: 50%;
    background: var(--signal-red);
  }
  .back-mark__name {
    margin-top: 26px;
    font-size: 48px;
    font-weight: 600;
    color: var(--paper);
    letter-spacing: 0.5px;
    white-space: nowrap;
  }
</style>
</head>
<body>
<main class="canvas">

  <section class="card card--front" aria-label="Business card front">
    <svg class="front-shape" width="700" height="400" viewBox="0 0 700 400" aria-hidden="true">
      <path d="M300 0 C 248 150, 270 290, 350 355 C 292 285, 282 150, 318 0 Z" fill="var(--ink)"/>
      <path d="M335 0 C 292 170, 330 320, 440 400 L 700 400 L 700 0 Z" fill="var(--ink)"/>
    </svg>

    <div class="brand-mark">
      <div class="brand-mark__circle"></div>
      <div class="brand-mark__name">Grant Felber</div>
    </div>

    <div class="contact">
      <h1 class="contact__name">Grant Felber</h1>
      <ul class="contact__list">
        <li class="contact__item">
          <svg width="20" height="14" viewBox="0 0 20 14" aria-hidden="true">
            <rect x="1" y="1" width="18" height="12" fill="none" stroke="var(--signal-red)" stroke-width="1.6"/>
            <path d="M1 1 L10 8 L19 1" fill="none" stroke="var(--signal-red)" stroke-width="1.6"/>
          </svg>
          <span>Grant.Felber@quorvamail.co.uk</span>
        </li>
        <li class="contact__item">
          <svg width="20" height="20" viewBox="0 0 20 20" aria-hidden="true">
            <circle cx="10" cy="10" r="8.5" fill="none" stroke="var(--signal-red)" stroke-width="1.6"/>
            <path d="M7 5.5 L8.6 7.6 L7.8 8.8 C8.5 10.3 9.7 11.5 11.2 12.2 L12.4 11.4 L14.5 13 L13.4 14.4 C10 14.2 5.8 10 5.6 6.6 Z" fill="var(--signal-red)"/>
          </svg>
          <span>+44 7700 382046</span>
        </li>
        <li class="contact__item">
          <svg width="20" height="20" viewBox="0 0 20 20" aria-hidden="true">
            <circle cx="10" cy="10" r="8.5" fill="none" stroke="var(--signal-red)" stroke-width="1.6"/>
          </svg>
          <span>@Grantfelber</span>
        </li>
      </ul>
    </div>
  </section>

  <section class="card card--back" aria-label="Business card back">
    <div class="back-mark">
      <div class="back-mark__circle"></div>
      <div class="back-mark__name">Grant Felber</div>
    </div>
  </section>

</main>
</body>
</html>
```